Business card design, sleek & clean . For a notary loan signing business. I work with several lenders escrow officers etc . I am bilingual in Spanish , work 7 days a week to meet clients needs. Loan documents can be emailed for printing.

Not sure sleek clean logo

```html
<!DOCTYPE html>
<html lang="en">
<head>
<meta charset="utf-8">
<title>Marisol Avendano – Business Card</title>
<link href="https://fonts.googleapis.com/css2?family=Cinzel:wght@500;600&family=Montserrat:wght@500;600&display=swap" rel="stylesheet">
<style>
  :root {
    --backdrop: #cbc9c1;
    --navy-deep: #0b0740;
    --navy: #231d5e;
    --navy-light: #2e2762;
    --gold-dark: #b8923e;
    --gold: #e9d58f;
    --gold-light: #f7ecb8;
    --white: #ffffff;
    --ink: #1a1650;
  }
  * { margin: 0; padding: 0; box-sizing: border-box; }
  html, body { width: 1200px; height: 867px; overflow: hidden; }
  body {
    background: var(--backdrop);
    display: flex;
    align-items: center;
    justify-content: center;
    gap: 60px;
    font-family: "Montserrat", sans-serif;
  }
  .card {
    position: relative;
    width: 500px;
    height: 286px;
    border-radius: 16px;
    overflow: hidden;
    box-shadow: 0 10px 24px rgba(0,0,0,0.22);
  }
  .gold-band {
    background: linear-gradient(90deg, var(--gold-dark), var(--gold) 35%, var(--gold-light) 60%, var(--gold) 80%, var(--gold-dark));
  }
  .brand-name {
    font-family: "Cinzel", serif;
    font-weight: 600;
    color: var(--gold);
    letter-spacing: 0.5px;
    white-space: nowrap;
  }
  .brand-title {
    font-family: "Cinzel", serif;
    font-weight: 500;
    color: var(--white);
    letter-spacing: 2px;
    text-transform: uppercase;
    white-space: nowrap;
  }

  /* Front */
  .card-front { background: var(--white); }
  .front-top {
    position: absolute; inset: 0 0 auto 0; height: 176px;
    background: linear-gradient(120deg, var(--navy-deep), var(--navy) 55%, var(--navy-light));
  }
  .front-identity { position: absolute; left: 34px; top: 34px; }
  .front-identity .brand-name { font-size: 30px; }
  .front-identity .brand-title { font-size: 9.5px; margin-top: 2px; }
  .front-language {
    margin-top: 12px; color: var(--white); font-weight: 600; font-size: 15px;
  }
  .front-band {
    position: absolute; left: 0; right: 0; top: 164px; height: 26px;
    display: flex; align-items: center; justify-content: flex-end; padding-right: 40px;
  }
  .front-band span {
    font-family: "Cinzel", serif; font-weight: 600; font-size: 13px;
    color: var(--ink); letter-spacing: 2px; text-transform: uppercase;
  }
  .front-rule {
    position: absolute; left: 0; top: 208px; width: 210px; height: 4px; background: var(--ink);
  }
  .contact-list {
    position: absolute; right: 22px; top: 206px; list-style: none;
    text-align: right;
  }
  .contact-list li {
    display: flex; align-items: center; justify-content: flex-end; gap: 8px;
    color: var(--ink); font-weight: 600; font-size: 15px; line-height: 24px;
  }
  .contact-icon { width: 17px; height: 17px; }

  /* Back */
  .card-back {
    background: linear-gradient(120deg, var(--navy-deep), var(--navy) 50%, var(--navy-light));
  }
  .back-band {
    position: absolute; top: 0; bottom: 0; left: 26px; width: 28px;
    display: flex; align-items: center; justify-content: center;
  }
  .back-band span {
    transform: rotate(-90deg); white-space: nowrap;
    font-family: "Cinzel", serif; font-weight: 600; font-size: 11px;
    color: var(--ink); letter-spacing: 1.5px; text-transform: uppercase;
  }
  .back-identity {
    position: absolute; left: 90px; right: 20px; top: 106px; text-align: center;
  }
  .back-identity .brand-name { font-size: 32px; }
  .back-identity .brand-title { font-size: 10.5px; margin-top: 4px; }
</style>
</head>
<body>
  <section class="card card-front" aria-label="Business card front">
    <div class="front-top"></div>
    <div class="front-identity">
      <p class="brand-name">Marisol Avendano</p>
      <p class="brand-title">Notary Public Loan Signing Agent</p>
      <p class="front-language">Hablo Espanol</p>
    </div>
    <div class="front-band gold-band"><span>Certified Loan Signing Agent</span></div>
    <div class="front-rule"></div>
    <ul class="contact-list">
      <li>(555)014-2290
        <svg class="contact-icon" viewBox="0 0 24 24" fill="none" stroke="#c9a24e" stroke-width="2" aria-hidden="true">
          <circle cx="12" cy="12" r="10"/>
          <path d="M8.5 7.5c0 4.5 3.5 8.5 8 8.5l1-2-2.5-1.2-1 1c-1.5-.6-3-2-3.6-3.6l1-1L10.2 6.5z"/>
        </svg>
      </li>
      <li>mavendano@example.com
        <svg class="contact-icon" viewBox="0 0 24 24" fill="none" stroke="#c9a24e" stroke-width="2" aria-hidden="true">
          <circle cx="12" cy="12" r="10"/>
          <circle cx="12" cy="12" r="3.5"/>
          <path d="M15.5 12v1.5a2 2 0 0 0 4 0V12a7.5 7.5 0 1 0-3 6"/>
        </svg>
      </li>
    </ul>
  </section>

  <section class="card card-back" aria-label="Business card back">
    <div class="back-band gold-band"><span>7 Days a Week to Meet Clients Needs.</span></div>
    <div class="back-identity">
      <p class="brand-name">Marisol Avendano</p>
      <p class="brand-title">Notary Public Loan Signing Agent</p>
    </div>
  </section>
</body>
</html>
```